Modern Design Business Card industrial maintenance company

Business card design for Company named Brookvale Equipment Services

Target Market(s)

Industrial

Industry/Entity Type

Maintenance and repair

Contact Information for Business Card

Place holder for address, office phone, mobile number and email

Requirements
Must have
• Clean modern look
Nice to have
• N/a

```html
<!DOCTYPE html>
<html lang="en">
<head>
<meta charset="UTF-8">
<title>Brookvale Equipment Services – Business Card</title>
<link href="https://fonts.googleapis.com/css2?family=Poppins:wght@300;400;600&display=swap" rel="stylesheet">
<style>
  :root {
    --backdrop: #222224;
    --card: #1e1e20;
    --ink: #ffffff;
    --ink-soft: #e6e6e6;
    --faint: #2c2c2f;
  }
  * { box-sizing: border-box; margin: 0; padding: 0; }
  html, body {
    width: 1200px; height: 780px; overflow: hidden;
    background: var(--backdrop);
    font-family: "Poppins", sans-serif;
    color: var(--ink);
  }
  .canvas {
    width: 1200px; height: 780px;
    display: flex; align-items: center; justify-content: center; gap: 40px;
  }
  .card {
    position: relative;
    width: 540px; height: 310px;
    background: var(--card);
    overflow: hidden;
    box-shadow: 0 14px 30px rgba(0,0,0,.45);
  }

  /* contact side */
  .card-contact .backdrop-ring {
    position: absolute; left: -70px; top: 30px;
    width: 330px; height: 330px;
  }
  .brand {
    display: flex; align-items: center; gap: 12px;
  }
  .brand-ring {
    width: 42px; height: 42px; border: 3px solid var(--ink); border-radius: 50%;
    flex: none;
  }
  .brand-name {
    font-weight: 600; line-height: 1.05; letter-spacing: .02em;
    text-transform: uppercase; color: var(--ink);
  }
  .card-contact .brand { position: absolute; right: 28px; top: 30px; }
  .card-contact .brand-name { font-size: 15px; }

  .contact-list {
    position: absolute; right: 28px; top: 104px;
    text-align: right; font-weight: 300; font-size: 13px; line-height: 1.45;
    color: var(--ink-soft);
  }
  .address { margin-bottom: 12px; }
  .contact-line { display: flex; justify-content: flex-end; align-items: center; gap: 9px; }
  .contact-line svg { width: 12px; height: 12px; flex: none; }

  .person { position: absolute; left: 30px; bottom: 32px; }
  .person-name { font-size: 26px; line-height: 1.1; }
  .person-name .first { font-weight: 600; }
  .person-name .last { font-weight: 300; }
  .person-role { font-size: 13px; font-weight: 300; margin-top: 4px; color: var(--ink-soft); }

  /* brand side */
  .card-brand { display: flex; align-items: center; justify-content: center; }
  .card-brand .brand { flex-direction: column; gap: 18px; }
  .card-brand .brand-ring { width: 96px; height: 96px; border-width: 5px; }
  .card-brand .brand-name { font-size: 24px; text-align: center; }
</style>
</head>
<body>
<main class="canvas">

  <section class="card card-contact">
    <svg class="backdrop-ring" viewBox="0 0 330 330" aria-hidden="true">
      <circle cx="165" cy="165" r="150" fill="none" stroke="var(--faint)" stroke-width="14"/>
    </svg>

    <div class="brand">
      <span class="brand-name">Brookvale<br>Equipment Services</span>
      <span class="brand-ring" aria-hidden="true"></span>
    </div>

    <div class="contact-list">
      <p class="address">1840 Ridgeway Ave. Suite 310<br>Dayton, OH 45402</p>
      <p class="contact-line">(937) 555-0142
        <svg viewBox="0 0 12 12" aria-label="Office phone"><path d="M3 1 L5 3.5 L4 4.8 Q5 7 7.2 8 L8.5 7 L11 9 L9.5 11 Q4 10.5 1 3 Z" fill="var(--ink)"/></svg>
      </p>
      <p class="contact-line">(937) 555-0187
        <svg viewBox="0 0 12 12" aria-label="Mobile"><rect x="3" y="0.5" width="6" height="11" rx="1.2" fill="none" stroke="var(--ink)" stroke-width="1.2"/><circle cx="6" cy="9.5" r=".7" fill="var(--ink)"/></svg>
      </p>
      <p class="contact-line">www.brookvale-es.com
        <svg viewBox="0 0 12 12" aria-label="Website"><circle cx="6" cy="6" r="5" fill="none" stroke="var(--ink)" stroke-width="1.1"/><ellipse cx="6" cy="6" rx="2.2" ry="5" fill="none" stroke="var(--ink)" stroke-width="1"/><line x1="1" y1="6" x2="11" y2="6" stroke="var(--ink)" stroke-width="1"/></svg>
      </p>
      <p class="contact-line">info@brookvale-es.com
        <svg viewBox="0 0 12 12" aria-label="Email"><rect x="0.8" y="2.5" width="10.4" height="7" fill="none" stroke="var(--ink)" stroke-width="1.1"/><path d="M1 3 L6 7 L11 3" fill="none" stroke="var(--ink)" stroke-width="1.1"/></svg>
      </p>
    </div>

    <div class="person">
      <p class="person-name"><span class="first">Mara</span> <span class="last">Ellison</span></p>
      <p class="person-role">Co-Founder &amp; CEO</p>
    </div>
  </section>

  <section class="card card-brand">
    <div class="brand">
      <span class="brand-ring" aria-hidden="true"></span>
      <span class="brand-name">Brookvale<br>Equipment Services</span>
    </div>
  </section>

</main>
</body>
</html>
```